App-Design für Vergleichsportal für Reparaturen
Zielgruppe
Flickwerkstatt ist das Vergleichsportal für Reparaturen in deiner Nähe. Egal ob du eine Werkstatt für dein Smartphone, Tablet, Laptop, Computer, Smartwatch oder Spielkonsole suchst. Mit uns findest du deine passende Reparaturwerkstat in deiner Nähe mit dem besten Preis für dich. Du kannst dich direkt über unser Portal deinen Reparaturauftrag erhalten und wirst durch unser Sicher Kaufen Käuferschutz und unser MONVIRA Treuhandschutz abgesichert.
Aufgabenstellung
Unter Flickwerkstatt.de kann das aktuelle Design angeschaut werden. Die Farbe sollten übernommen werden.
Über die Startseite kann der Kunde sein Gerät, Service sowie seine Adresse eingeben. Auf der Vergleichsseite bekommt der Kunde die Übersicht welche Reparaturwerkstätten es gibt, zu welche Preisen die ausgewählte Dienstleistung angeboten wird. Wenn der Kunde auf den Button 'Jetzt Online Bestpreis buchen' drückt, dann kommt der Kunde in den Warenkorb. Im Warenkorb können noch weitere Dienstleistungen und Produkte dazugebucht werden. Und anschließend kommt der Kunde in die Kasse und kann der Bestellvorgang beenden. Die Benutzerführung sollte einfach sein. Im Fokus steht die Vergleichsseite. Dort sollte der Kunde ca. 4 Werkstätten auf einen Blick sehen können. Könnte ausschauen wie bei Wahlblick9 in der Kategorie Mobilfunk.
Die Vergleichseite sollte auf jeden Fall folgende Elemente enthalten:
- Entfernung zur Werkstatt in Meter bzw. Kilometer
- Logo der Werkstatt
- Name der Werkstatt
- Bewertungssterne der Werkstatt
- Reparaturzeit und Ersatzeilverfügbarkeit
- Reparaturpreis (Platz sollte auch bei Auswahl von 2 Dienstleistungen vorhanden sein)
- Rabattanzeige
- Qualitätssiegel (noch nicht vorhanden)
- Anzeige von Verknappung (z. B. noch 3 Termin frei)
- Qualitätsmerkmale (z. B. 12 Monate Garantie)
Die Merkmale Öffnungszeiten, Adresse, Kostenpflichtige Zusatzleistungen können aus Platzgründen in den Warenkorbseite wandern außer es gibt eine schöne und einfache Lösung.
In der Warenkorbseite kann dazu auch die Wahlblick9 Seite dienen.
Bei allen sollte auf die Benutzerfreundlichkeit geachtet werden.
Bei offenen Frage stehe ich zur Verfügung und freue mich auf viele Designs.
Vielen DANK im Voraus!

```html
<!DOCTYPE html>
<html lang="de">
<head>
<meta charset="utf-8">
<title>Flickwerkstatt – Display Original-Qualität</title>
<link href="https://fonts.googleapis.com/css2?family=Source+Sans+3:wght@300;400;600;700&display=swap" rel="stylesheet">
<style>
  :root{
    --stage:#2b2b2b;
    --teal:#1f3f4c;
    --green:#8dc63f;
    --green-dark:#5e8f2a;
    --grey:#bdbdbd;
    --white:#ffffff;
    --ink:#262626;
    --muted:#6d6d6d;
  }
  *{box-sizing:border-box;margin:0;padding:0}
  html,body{width:1200px;height:728px;overflow:hidden}
  body{background:var(--stage);font-family:"Source Sans 3",sans-serif;color:var(--ink);position:relative}
  .screen{
    position:absolute;left:50%;top:50%;width:375px;height:812px;
    transform:translate(-50%,-50%) scale(0.86);
    background:var(--grey);overflow:hidden;
  }
  .status-bar{height:34px;background:var(--white);display:flex;align-items:center;justify-content:space-between;padding:0 16px 0 18px;font-weight:600;font-size:15px}
  .status-icons{display:flex;gap:5px;align-items:center}
  .app-header{height:47px;background:var(--white);display:flex;align-items:center;justify-content:space-between;padding:0 14px 8px 14px}
  .brand{display:flex;align-items:center;gap:6px;font-size:17px;font-weight:400;color:var(--green-dark)}
  .brand-dot{width:14px;height:14px;border-radius:50%;background:var(--green)}
  .menu{width:24px;display:flex;flex-direction:column;gap:6px}
  .menu span{height:2px;background:var(--teal);display:block}
  .hero{height:82px;background:var(--teal);text-align:center;padding-top:25px}
  .hero-title{color:var(--green);font-weight:700;font-size:12.5px}
  .hero-sub{color:var(--green);font-size:10.5px;margin-top:4px;font-weight:400}
  .card-behind{position:absolute;left:29px;top:201px;width:316px;height:30px;background:#d6d6d6;font-size:11px;color:#555;padding:12px 12px 0}
  .detail-card{position:absolute;left:29px;top:221px;width:316px;box-shadow:0 2px 8px rgba(0,0,0,.15)}
  .detail-head{height:57px;background:var(--teal);display:flex;align-items:center;justify-content:space-between;padding:0 16px;color:var(--white);font-size:14.5px;font-weight:300}
  .detail-title{display:flex;align-items:center;gap:7px}
  .detail-body{position:relative;background:var(--white);height:361px;overflow:hidden;padding:28px 26px 0 16px;font-size:10.6px;line-height:1.36;font-weight:300}
  .detail-body p{margin-bottom:14px}
  .detail-body strong{font-weight:600;color:var(--teal)}
  .label{font-weight:400;color:var(--ink)}
  .detail-body::after{content:"";position:absolute;left:0;right:0;bottom:0;height:22px;background:linear-gradient(rgba(255,255,255,0),#fff)}
  .scroll-track{position:absolute;right:6px;top:22px;bottom:10px;width:1px;background:#e2e2e2}
  .scroll-thumb{position:absolute;right:4px;top:22px;width:6px;height:200px;border-radius:3px;background:var(--green)}
  .detail-foot{height:17px;background:var(--teal)}
  .trust-row{position:absolute;top:692px;left:0;right:0;display:flex;justify-content:space-around;padding:0 30px}
  .trust{display:flex;flex-direction:column;align-items:center;gap:8px;font-size:9px;color:var(--ink)}
</style>
</head>
<body>
  <main class="screen">
    <div class="status-bar">
      <span>9:41</span>
      <span class="status-icons">
        <svg width="17" height="11" viewBox="0 0 17 11"><rect x="0" y="7" width="3" height="4" fill="#222"/><rect x="4.5" y="5" width="3" height="6" fill="#222"/><rect x="9" y="2.5" width="3" height="8.5" fill="#222"/><rect x="13.5" y="0" width="3" height="11" fill="#222"/></svg>
        <svg width="15" height="11" viewBox="0 0 15 11"><path d="M7.5 10.5 L5 8 A3.5 3.5 0 0 1 10 8 Z" fill="#222"/><path d="M2.5 5.5 A7 7 0 0 1 12.5 5.5" stroke="#222" stroke-width="1.6" fill="none"/><path d="M0.5 3 A10 10 0 0 1 14.5 3" stroke="#222" stroke-width="1.6" fill="none"/></svg>
        <svg width="24" height="11" viewBox="0 0 24 11"><rect x="0.5" y="0.5" width="21" height="10" rx="2.5" fill="none" stroke="#222"/><rect x="2" y="2" width="18" height="7" rx="1.2" fill="#222"/><rect x="22.3" y="3.5" width="1.5" height="4" fill="#222"/></svg>
      </span>
    </div>
    <header class="app-header">
      <div class="brand"><span class="brand-dot"></span>Flickwerkstatt</div>
      <div class="menu"><span></span><span></span><span></span></div>
    </header>
    <section class="hero">
      <div class="hero-title">Reparaturen Im Vergleich, in deiner Nähe!</div>
      <div class="hero-sub">Garantiert die besten Tarife</div>
    </section>

    <div class="card-behind">Reparaturkategorie wählen</div>
    <article class="detail-card">
      <div class="detail-head">
        <span class="detail-title">
          <svg width="14" height="14" viewBox="0 0 14 14"><circle cx="7" cy="7" r="6.5" fill="#fff"/><rect x="6.1" y="6" width="1.8" height="4.8" fill="#1f3f4c"/><circle cx="7" cy="4" r="1.1" fill="#1f3f4c"/></svg>
          Display Original-Qualität
        </span>
        <svg width="14" height="12" viewBox="0 0 14 12"><path d="M13 6H2M6 1.5L1.5 6L6 10.5" stroke="#8dc63f" stroke-width="1.4" fill="none"/></svg>
      </div>
      <div class="detail-body">
        <p class="label">Beschreibung:</p>
        <p>Das Glas von deinem Gerät ist gesplittet. Das gesplitterte Display bleibt schwarz, oder aber du kannst das Gerät noch bedienen. Auf dem Bildschirm werden Streifen oder schwarze Pixel angezeigt.</p>
        <p><span class="label">HINWEIS:</span> Wenn du deinen Bildschirm nicht per Touch bedienen kannst, aber das Glas nicht gesplittet ist, dann liegt hier wahrscheinlich ein Chipfehler vor. Der Chip Touch IC wird ausgetauscht und verlötet. Wähle hierzu bitte den Punkt <strong>Chip Touch IC.</strong></p>
        <p><span class="label">HINWEIS:</span> Wenn das Display dunkel ist und der Inhalt nur unter direktem Licht sichtbar ist und du die Helligkeit deines Displays nicht erhöhen kannst, dann liegt in diesem Fallwahrscheinlich ein Chipfehler vor. Der Chip Backlight IC wird ausgetauscht und verlötet. Wähle hierzu bitte den Punkt <strong>Chip Backlight IC.</strong></p>
        <p style="margin-bottom:0"><span class="label">Ersatzteilqualität:</span><br>Bei der Auswahl von <strong>Display Original-Qualität</strong> wird ein Display folgender Qualitätskriterien eingebaut:</p>
        <span class="scroll-track"></span>
        <span class="scroll-thumb"></span>
      </div>
      <div class="detail-foot"></div>
    </article>

    <section class="trust-row">
      <div class="trust">
        <svg width="56" height="66" viewBox="0 0 56 66"><path d="M28 3 L52 11 V34 C52 50 40 59 28 63 C16 59 4 50 4 34 V11 Z" fill="none" stroke="#5e8f2a" stroke-width="4"/><path d="M28 9 L46 15 V34 C46 46 37 53 28 56 C19 53 10 46 10 34 V15 Z" fill="none" stroke="#8dc63f" stroke-width="1.5"/><text x="28" y="43" text-anchor="middle" font-size="24" font-family="Source Sans 3, sans-serif" fill="#1f3f4c">€</text></svg>
        Käuferschutz
      </div>
      <div class="trust">
        <svg width="56" height="66" viewBox="0 0 56 66"><path d="M28 3 L52 11 V34 C52 50 40 59 28 63 C16 59 4 50 4 34 V11 Z" fill="none" stroke="#5e8f2a" stroke-width="4"/><path d="M28 9 L46 15 V34 C46 46 37 53 28 56 C19 53 10 46 10 34 V15 Z" fill="none" stroke="#8dc63f" stroke-width="1.5"/><path d="M15 30 L22 24 L30 27 L36 23 L42 29 L33 39 L26 34 Z" fill="none" stroke="#1f3f4c" stroke-width="1.5" stroke-linejoin="round"/><path d="M24 33 L28 37 M27 31 L31 35" stroke="#1f3f4c" stroke-width="1.3"/></svg>
        Treuhandschutz
      </div>
      <div class="trust">
        <svg width="56" height="66" viewBox="0 0 56 66"><path d="M28 3 L52 11 V34 C52 50 40 59 28 63 C16 59 4 50 4 34 V11 Z" fill="none" stroke="#5e8f2a" stroke-width="4"/><path d="M28 9 L46 15 V34 C46 46 37 53 28 56 C19 53 10 46 10 34 V15 Z" fill="none" stroke="#8dc63f" stroke-width="1.5"/><path d="M22.5 30 V25 A5.5 5.5 0 0 1 33.5 25 V30" fill="none" stroke="#1f3f4c" stroke-width="1.6"/><rect x="19.5" y="30" width="17" height="14" rx="2" fill="none" stroke="#1f3f4c" stroke-width="1.6"/><circle cx="28" cy="36" r="1.8" fill="#1f3f4c"/><rect x="27.3" y="37" width="1.4" height="4" fill="#1f3f4c"/></svg>
        Datenschutz
      </div>
    </section>
  </main>
</body>
</html>
```